Lower Cost Storage Scheme Email marketing campaign for Corvel Energy

Design a visually engaging and professional marketing email to promote the upcoming Federal Government Battery Subsidy to our existing solar clients, encouraging them to install a battery system now to maximise savings. email content example "Subject: ⚡ Federal Government Battery Subsidy is Coming – Maximise Your Solar Savings

Body:
Hi [First Name],

Great news! With the federal election now decided, the Federal Government’s Home Battery Subsidy Program is officially on the way.

While the scheme hasn’t formally launched yet, it's guaranteed—and like the solar rebate before it, the subsidy reduces each year, so the earlier you install, the more you’ll save.

Crucially, the subsidy is only available once per household, so it makes sense to install a system that fully meets your home's battery needs right from the start.

Why add a battery to your existing solar system now?
✅ Store your excess solar energy instead of sending it back to the grid for low feed-in tariffs
✅ Use your stored solar power at night, when electricity prices are highest (typically 5–8pm)
✅ Slash your power bills and avoid rising time-of-use charges
✅ Protect your home from power outages
✅ Increase your self-sufficiency and long-term energy security

If you’ve already installed solar with us, now is the ideal time to complete your setup with a battery system designed to maximise your return—and take full advantage of this one-off federal subsidy.

Call us today or reply to this email to secure your spot and beat the rush.

Let your solar work smarter for your home,
The Corvel Energy Team"

Target Market(s)

Content: We’ve provided the copy (see attached or below). The key points to emphasise in the design are: The urgency (subsidy winds down each year, limited to one per household). The benefits of installing a battery now, including energy savings, time-of-use charge avoidance, and self-sufficiency. Call to action: “Call us today or reply to this email to secure your spot and beat the rush.”

Industry/Entity Type

Renewable Energy

Colors
0054AA
0677BA
7BADD7
CADEEF
E8F1F8
EB3D1F
EC4F4E
F09395
F8D3D4
FCEDEE

Requirements
Must have
• Clean, modern, and trustworthy – aligned with Corvel Energy branding. Bold headers and icons to make key points stand out. Include visual elements such as: A solar battery image Infographic or icon-style section showing key battery benefits (e.g. bill savings, backup power, self-consumption) Highlighted call-to-action button (“Secure My Battery Now” or “Beat the Rush”)
Nice to have
• I would like to have our company imagery (Corvel Energy) alongside the battery brands we offer being Velto, QMP, Brimlite and TervoPWR
Should not have
• Unsure

```html
<!DOCTYPE html>
<html lang="en">
<head>
<meta charset="UTF-8">
<title>Federal Government Battery Subsidy – Corvel Energy</title>
<link rel="stylesheet" href="https://fonts.googleapis.com/css2?family=Poppins:wght@400;500;600;700;800&display=swap">
<style>
  :root {
    --navy: #0d2f52;
    --navy-deep: #0a2745;
    --red: #e01f1f;
    --red-dark: #c81616;
    --card: #f5f6f8;
    --page: #eceef1;
    --tile: #e9ecf0;
    --text: #0f2a47;
    --white: #ffffff;
  }
  * { box-sizing: border-box; margin: 0; padding: 0; }
  html, body { width: 720px; height: 1200px; overflow: hidden; }
  body {
    font-family: "Poppins", Arial, sans-serif;
    background: var(--page);
    color: var(--text);
    position: relative;
  }
  .hero {
    position: absolute; left: 0; top: 0; width: 720px; height: 400px;
    background:
      radial-gradient(ellipse at 62% 68%, rgba(255,214,150,.55) 0%, rgba(255,214,150,0) 38%),
      linear-gradient(180deg, #3d4f6a 0%, #5a6f8c 30%, #7e8fa6 52%, #4b5563 72%, #2b3b2e 100%);
  }
  .hero-title {
    position: absolute; left: 68px; top: 28px; width: 520px;
    color: var(--white); font-weight: 700; font-size: 34px; line-height: 1.28;
    letter-spacing: -0.2px;
  }
  .hero-title svg { width: 24px; height: 30px; vertical-align: -3px; margin-right: 4px; }
  .badge {
    position: absolute; left: 66px; top: 232px; width: 150px; height: 60px;
    background: var(--red); color: var(--white); border-radius: 4px;
    font-weight: 600; font-size: 20px; line-height: 1.2; text-align: center;
    display: flex; align-items: center; justify-content: center;
  }
  .card {
    position: absolute; left: 50px; top: 342px; width: 620px; height: 880px;
    background: var(--card); border-radius: 30px 30px 0 0;
  }
  .intro { position: absolute; left: 19px; top: 24px; width: 590px; font-size: 17.5px; line-height: 1.3; }
  .intro strong { font-weight: 700; display: block; }
  .benefits {
    position: absolute; left: 12px; top: 150px; display: flex; gap: 3px;
  }
  .benefit {
    width: 116px; height: 138px; background: var(--tile); border-radius: 8px;
    box-shadow: 0 2px 4px rgba(0,0,0,.08);
    display: flex; flex-direction: column; align-items: center; padding-top: 12px;
    text-align: center;
  }
  .benefit-icon {
    width: 58px; height: 58px; border-radius: 50%; background: var(--navy);
    display: flex; align-items: center; justify-content: center;
  }
  .benefit-icon svg { width: 34px; height: 34px; }
  .benefit-label { margin-top: 10px; font-weight: 600; font-size: 14px; line-height: 1.15; padding: 0 4px; }
  .body-copy {
    position: absolute; left: 18px; top: 312px; width: 584px;
    font-size: 17.5px; line-height: 1.3; text-align: center;
  }
  .urgency {
    position: absolute; left: 29px; top: 446px; width: 562px; height: 108px;
    background: var(--navy); border-radius: 14px;
    box-shadow: 0 3px 6px rgba(0,0,0,.2);
    color: var(--white); text-align: center; font-weight: 600; font-size: 19px; line-height: 1.3;
    padding-top: 10px;
  }
  .urgency svg { width: 40px; height: 42px; display: block; margin: 0 auto 4px; }
  .cta {
    position: absolute; left: 116px; top: 570px; width: 388px; height: 88px;
    background: var(--red); border-radius: 14px; color: var(--white); text-align: center;
    box-shadow: 0 3px 6px rgba(0,0,0,.15);
    padding-top: 8px; text-decoration: none; display: block;
  }
  .cta-main { font-weight: 700; font-size: 25px; line-height: 1.3; }
  .cta-sub { font-weight: 500; font-size: 14px; line-height: 1.25; }
  .company {
    position: absolute; left: 0; top: 688px; width: 620px;
    display: flex; justify-content: center; align-items: center; gap: 10px;
    font-weight: 700; font-size: 24px; color: var(--navy);
  }
  .company-mark { width: 34px; height: 34px; background: var(--navy); }
  .brands {
    position: absolute; left: 8px; top: 748px; width: 604px;
    display: flex; justify-content: space-between; align-items: center;
    font-weight: 700; font-size: 30px; color: var(--navy-deep); padding: 0 8px;
  }
  .signoff {
    position: absolute; left: 0; top: 820px; width: 620px; text-align: center;
    color: var(--red); font-weight: 700; font-size: 14px; letter-spacing: .2px;
  }
</style>
</head>
<body>
  <div class="hero" role="img" aria-label="Modern home at dusk with rooftop solar panels and a wall-mounted home battery glowing green"></div>
  <h1 class="hero-title"><svg viewBox="0 0 24 30"><path d="M14 0 L3 17 H11 L8 30 L21 11 H13 Z" fill="#fff"/></svg>Federal Government Battery Subsidy is Here - Save More Now.</h1>
  <div class="badge">Reduces<br>Every Year</div>

  <main class="card">
    <p class="intro"><strong>Great news!</strong>The Federal Government’s Home Battery Subsidy Program is confirmed and launching soon. Like the solar rebate before it, this subsidy will reduce each year – so the earlier you act, the more you’ll save.</p>

    <ul class="benefits" style="list-style:none">
      <li class="benefit">
        <span class="benefit-icon"><svg viewBox="0 0 34 34"><text x="17" y="27" text-anchor="middle" font-family="Poppins, Arial, sans-serif" font-weight="700" font-size="28" fill="#fff">$</text></svg></span>
        <span class="benefit-label">Slash Your Power Bills</span>
      </li>
      <li class="benefit">
        <span class="benefit-icon"><svg viewBox="0 0 34 34"><rect x="10" y="6" width="14" height="24" rx="2" fill="none" stroke="#fff" stroke-width="2"/><rect x="14" y="3" width="6" height="3" fill="#fff"/><rect x="13" y="18" width="8" height="9" fill="#fff"/><circle cx="17" cy="12" r="2.5" fill="#f5c542"/></svg></span>
        <span class="benefit-label">Store Excess Solar Energy</span>
      </li>
      <li class="benefit">
        <span class="benefit-icon"><svg viewBox="0 0 34 34"><path d="M6 17 L17 8 L28 17 V29 H6 Z" fill="none" stroke="#fff" stroke-width="2"/><rect x="14" y="19" width="6" height="6" fill="none" stroke="#fff" stroke-width="1.6"/><path d="M12 3 a4 4 0 1 0 4 5 a3 3 0 1 1 -4 -5z" fill="#fff"/></svg></span>
        <span class="benefit-label">Use Power at Night</span>
      </li>
      <li class="benefit">
        <span class="benefit-icon"><svg viewBox="0 0 34 34"><path d="M17 3 L28 7 V16 C28 23 23 28 17 31 C11 28 6 23 6 16 V7 Z" fill="#fff"/><path d="M19 9 L12 18 H17 L15 25 L22 15 H17 Z" fill="#0d2f52"/></svg></span>
        <span class="benefit-label">Protection from Outages</span>
      </li>
      <li class="benefit">
        <span class="benefit-icon"><svg viewBox="0 0 34 34"><path d="M5 16 L16 7 L27 16 V28 H5 Z" fill="none" stroke="#fff" stroke-width="2"/><rect x="13" y="18" width="6" height="6" fill="none" stroke="#fff" stroke-width="1.6"/><circle cx="26" cy="26" r="5" fill="#fff"/><path d="M23.5 26 L25.5 28 L28.5 24" fill="none" stroke="#0d2f52" stroke-width="1.6"/></svg></span>
        <span class="benefit-label">One-Time Subsidy per Household</span>
      </li>
    </ul>

    <p class="body-copy">This is a limited-time opportunity. Act now before the subsidy decreases!If you’ve already installed solar with us, now is the ideal time to complete your setup with a battery system designed to maximise your return—and take full advantage of this one-off federal subsidy.</p>

    <div class="urgency">
      <svg viewBox="0 0 40 42"><path d="M8 3 H32 M8 39 H32" stroke="#fff" stroke-width="3"/><path d="M11 4 C11 16 29 16 29 4 M11 38 C11 26 29 26 29 38 M11 4 C11 14 20 18 20 21 C20 24 11 28 11 38 M29 4 C29 14 20 18 20 21 C20 24 29 28 29 38" fill="none" stroke="#fff" stroke-width="2.4"/><path d="M14 37 L20 30 L26 37 Z" fill="#fff"/></svg>
      This is a limited-time opportunity. Act now before the<br>subsidy decreases!
    </div>

    <a class="cta" href="#">
      <div class="cta-main">Secure My Battery Now</div>
      <div class="cta-sub">Or call us today to speak with a<br>battery expert.</div>
    </a>

    <div class="company"><span class="company-mark"></span>Corvel Energy</div>

    <div class="brands">
      <span>Velto</span>
      <span>QMP</span>
      <span>Brimlite</span>
      <span>TervoPWR</span>
    </div>

    <p class="signoff">THE CORVEL ENERGY TEAM</p>
  </main>
</body>
</html>
```